PowerPoint presentation

Please clean up this presentation using the overall look of Brovane's brand. www.brovanereit.com. Looking for clean, contemporary, easy to read.

This presentation will be sent to customers to educate them about resources available to them for cost and energy savings.

```html
<!DOCTYPE html>
<html lang="en">
<head>
<meta charset="utf-8">
<title>E-Playbook – Brovane</title>
<link href="https://fonts.googleapis.com/css2?family=Poppins:wght@400;500;600;700&display=swap" rel="stylesheet">
<style>
:root{
  --canvas:#0a1a4a;
  --navy:#123a8f;
  --ink:#1b2a4a;
  --muted:#4a5a78;
  --sky:#b9cfe8;
  --pale:#dff0fa;
  --pale-green:#d6efe0;
  --deep:#0b2d8f;
  --mid:#2c65c0;
  --accent:#2f6fc6;
  --light:#6aa5dc;
  --red:#d3333a;
  --grey:#efefef;
}
*{margin:0;padding:0;box-sizing:border-box}
html,body{width:720px;height:1200px;overflow:hidden;background:var(--canvas)}
body{font-family:'Poppins',sans-serif;color:var(--ink);position:relative}
.slide{position:absolute;overflow:hidden;background:#fff}
.abs{position:absolute}
.cover{left:49px;top:15px;width:621px;height:466px;background:var(--sky)}
.cover .draft{left:44px;top:36px;font-size:10px;color:#2a2f3a;font-weight:500}
.cover .title{left:44px;top:54px;font-size:22px;font-weight:700;color:var(--navy)}
.cover .url{left:44px;top:87px;font-size:8px;color:#2a2f3a}
.cover .brand{right:46px;top:58px;display:flex;align-items:center;gap:6px;font-size:20px;font-weight:700;color:var(--navy)}
.cover .brand i{width:16px;height:16px;background:var(--navy);display:block}
.cover .photo{left:0;right:0;top:180px;bottom:0;background:linear-gradient(180deg,var(--sky) 0%,#9fb3c9 25%,#8797a8 60%,#6f8a58 82%,#4e7a34 100%)}
.small{width:305px;height:227px}
.s-purpose{left:49px;top:489px}
.s-team{left:366px;top:489px}
.s-vendors{left:49px;top:722px}
.s-levels{left:366px;top:722px;background:var(--deep)}
.s-rule{left:49px;top:957px}
.s-talk{left:366px;top:957px;background:var(--mid)}
.heading{font-weight:700;color:var(--navy);font-size:9px;line-height:1.3}
.foot{left:19px;bottom:6px;font-size:5px;font-weight:700;color:var(--navy);display:flex;align-items:center;gap:2px}
.foot i{width:5px;height:5px;background:var(--navy);display:block}
.pgnum{right:19px;bottom:7px;font-size:4px;color:var(--muted)}
.s-levels .foot,.s-levels .pgnum{color:#fff}
.s-levels .foot i{background:#fff}
.body5{font-size:5px;line-height:1.35;color:var(--ink)}
.lbl{font-size:4.8px;line-height:1.3;text-align:center;width:92px}
.lbl b{font-weight:700}
.row{position:absolute;left:19px;width:271px;background:var(--pale);border-radius:2px}
.row .rh{position:absolute;left:5px;font-size:5px;font-weight:700;color:var(--navy);line-height:1.2}
.person{position:absolute;display:flex;align-items:center;gap:3px;font-size:3.8px;line-height:1.25;color:var(--muted)}
.person b{display:block;color:var(--navy);font-size:4.2px}
.avatar{width:15px;height:15px;border-radius:50%;background:linear-gradient(180deg,#c7b7a6,#8d7a68)}
.adv{position:absolute;top:27px;width:60px;font-size:3.2px;line-height:1.3;color:var(--muted)}
.adv b{display:block;color:var(--navy);font-size:4px;line-height:1.25}
.adv .nm{color:var(--accent);font-size:3.6px;margin:3px 0 2px}
.vendor{position:absolute;transform:translate(-50%,-50%);font-size:6px;font-weight:600;color:#2a3d6b;white-space:nowrap}
.lvl-txt{position:absolute;left:122px;width:175px;font-size:5px;line-height:1.35;color:#fff}
.lvl-line{position:absolute;left:115px;right:0;height:0.5px;background:rgba(255,255,255,.35)}
.pct{position:absolute;left:53px;color:#fff;font-weight:700}
.pct sup{font-size:.4em;font-weight:500;vertical-align:top}
.cells{position:absolute;left:19px;width:177px;display:grid;gap:1.5px}
.cell{background:var(--pale);text-align:center;padding-top:2px;height:17px}
.cell .v{font-size:6px;color:var(--navy);line-height:1}
.cell .v sup{font-size:3px}
.cell .k{font-size:3.6px;color:var(--muted)}
.green .cell{background:var(--pale-green)}
.sub6{font-size:4.6px;font-weight:700;color:var(--ink)}
.bullets{position:absolute;left:19px;top:148px;width:180px;list-style:none}
.bullets li{font-size:3.6px;line-height:1.3;padding-left:6px;position:relative;margin-bottom:1.3px}
.bullets li::before{content:"";position:absolute;left:0;top:1.3px;width:2.4px;height:2.4px;background:var(--navy);transform:rotate(45deg)}
.side{position:absolute;left:206px;top:0;right:0;bottom:0;background:var(--grey)}
.rule-title{left:19px;top:21px;font-size:7.6px;white-space:nowrap;z-index:1}
.chart{position:absolute;left:10px;width:80px;height:50px;background:#fff}
.chart .ct{position:absolute;left:3px;top:2px;font-size:3.4px;font-weight:600}
.chart .leg{position:absolute;font-size:2.6px;color:var(--muted);line-height:1.6}
.talk-brand{left:0;right:0;top:32px;text-align:center;font-size:12px;font-weight:700;color:#fff}
.talk-brand i{display:inline-block;width:8px;height:8px;background:#fff;margin-right:4px;vertical-align:0}
.talk-title{left:0;right:0;top:76px;text-align:center;color:#fff;line-height:1.25}
.talk-title .l1{font-size:14.5px;font-weight:400}
.talk-title .l2{font-size:15px;font-weight:700}
.people{left:61px;top:148px;width:165px;height:79px;border-radius:80px 80px 0 0;background:linear-gradient(180deg,#3f78cf,#2558ad)}
</style>
</head>
<body>

<section class="slide cover">
  <div class="abs draft">DRAFT 2.7.25</div>
  <h1 class="abs title">E-Playbook</h1>
  <div class="abs url">www.brovanereit.com</div>
  <div class="abs brand"><i></i>Brovane</div>
  <div class="abs photo" role="img" aria-label="Photograph of a single-storey senior living community building with a gabled entrance canopy, stone base and green lawn"></div>
</section>

<section class="slide small s-purpose">
  <h2 class="abs heading" style="left:19px;top:17px;width:262px">The E-Playbook purpose is to operationalize Brovane's commitment to supporting our tenant operators' efficient and sustainable practices.</h2>
  <p class="abs body5" style="left:19px;top:58px;width:270px">Working with our Operators, Third-Party Advisors, and Preferred Vendors, Brovane has established consistent and comprehensive practices and approaches that can be replicated and scaled.</p>
  <svg class="abs" style="left:0;top:0" width="305" height="227" viewBox="0 0 305 227">
    <g stroke="#555" stroke-width="0.4">
      <line x1="105" y1="96" x2="114" y2="96"/><line x1="105" y1="131" x2="114" y2="131"/><line x1="105" y1="164" x2="114" y2="164"/>
      <line x1="167" y1="113" x2="182" y2="113"/><line x1="167" y1="147" x2="182" y2="147"/><line x1="167" y1="184" x2="182" y2="184"/>
    </g>
    <g>
      <polygon points="131,79 148,96 131,113 114,96" fill="#3d83d6"/>
      <polygon points="150,96 167,113 150,130 133,113" fill="#6aa5dc"/>
      <polygon points="131,113 148,130 131,147 114,130" fill="#2f6fc6"/>
      <polygon points="150,130 167,147 150,164 133,147" fill="#6aa5dc"/>
      <polygon points="131,147 148,164 131,181 114,164" fill="#3d83d6"/>
      <polygon points="150,167 167,184 150,201 133,184" fill="#2a5fb5"/>
    </g>
    <g fill="#fff"><circle cx="131" cy="96" r="3"/><circle cx="150" cy="113" r="3"/><circle cx="131" cy="130" r="3"/><circle cx="150" cy="147" r="3"/><circle cx="131" cy="164" r="3"/><circle cx="150" cy="184" r="3"/></g>
  </svg>
  <div class="abs lbl" style="left:16px;top:83px"><b>Practical and holistic</b><br>whole-building approach to energy and water efficiency opportunities</div>
  <div class="abs lbl" style="left:16px;top:117px"><b>Responsive and collaborative</b> services from upfront advice to project assessment and solutions to project support and management.</div>
  <div class="abs lbl" style="left:16px;top:161px"><b>Access</b><br>to rebates, incentives, and financing from Brovane and other third parties</div>
  <div class="abs lbl" style="left:182px;top:92px;width:94px"><b>Knowledgeable and vetted</b><br>third-party advisors and vendors with technical expertise and proven experience in the senior living and care space, REIT structure, and Brovane.</div>
  <div class="abs lbl" style="left:182px;top:133px;width:94px"><b>Best practices</b><br>including established and innovative new technologies, implemented successfully across other senior living and care properties and organizations.</div>
  <div class="abs lbl" style="left:182px;top:177px;width:94px"><b>Awareness</b><br>and support around evolving benchmarking and other regulatory compliance</div>
  <div class="abs foot"><i></i>Brovane</div>
  <div class="abs pgnum">2</div>
</section>

<section class="slide small s-team">
  <h2 class="abs heading" style="left:19px;top:18px">E-Playbook Team</h2>
  <p class="abs" style="left:19px;top:33px;width:260px;font-size:4.6px;line-height:1.35;color:var(--navy)">Brovane provides a collaborative team that knows the opportunities and challenges of efficient and sustainable practices as well as the nuances of senior living and care</p>
  <div class="row" style="top:48px;height:26px">
    <div class="rh" style="top:7px">Brovane<br>Management</div>
    <div class="person" style="left:58px;top:5px"><span class="avatar" role="img" aria-label="Portrait of Lena Harwood"></span><span><b>Lena Harwood</b>Sustainability</span></div>
    <div class="person" style="left:120px;top:5px"><span class="avatar" role="img" aria-label="Portrait of Owen Pratt"></span><span><b>Owen Pratt</b>Facilities and<br>Capital Projects</span></div>
    <div class="person" style="left:180px;top:5px"><span class="avatar" role="img" aria-label="Portrait of Carla Vance"></span><span><b>Carla Vance</b>Asset Management</span></div>
  </div>
  <div class="row" style="top:77px;height:26px">
    <div class="rh" style="top:6px">Program<br>Advisor</div>
    <div class="abs" style="left:68px;top:4px;width:196px;font-size:3.6px;line-height:1.35;color:var(--muted)"><b style="color:var(--navy);font-size:4.2px">Miles Brennan,</b> <span style="color:var(--accent);font-size:4px">Ashcombe Advisory</span><br>over 30 years of senior real estate expertise, providing a broad range of sustainability practices, leadership, and access to a preferred vendor network, including technical advisors</div>
  </div>
  <div class="row" style="top:106px;height:82px">
    <div class="rh" style="top:5px">Technical Advisors</div>
    <div class="abs" style="left:5px;top:12px;width:262px;font-size:3.2px;line-height:1.3;color:var(--muted)">Trusted and seasoned advisors with engagement and domain expertise across the prop-tech, health-tech, benchmarking, and renewable sectors of senior living and care</div>
    <div class="adv" style="left:5px"><b>Quillmont<br>Energy Group</b><div class="nm">Paul Dorsey and Neil Fontaine</div>providing ongoing advice and consultation to owners and operators. Helped implement large lighting, water, and HVAC projects for healthcare REITs over the last two years.</div>
    <div class="adv" style="left:69px"><b>Orvella Care<br>Advisory Services</b><div class="nm">Grace Whitlow</div>former chief clinical officer with 30-year experience improving quality and business results through strategic planning, innovation, and application of health-tech solutions, including fall management and vital sign monitoring</div>
    <div class="adv" style="left:142px"><b>Verdalux</b><div class="nm" style="margin-top:7px">Ilse Moravec</div>team includes certified energy auditors, certified energy managers, and energy and water data analysts. They provide utility collection, verification, portfolio integration, benchmarking, and energy audits for owners and operators.</div>
    <div class="adv" style="left:212px;width:55px"><b>Solvantis</b><div class="nm" style="margin-top:7px">Jordan Pike</div>former CFO/CPA with 20 years of real estate and solar experience, helping owners and operators evaluate the pros and cons of solar applications.</div>
  </div>
  <div class="row" style="top:191px;height:17px">
    <div class="abs" style="left:5px;top:3px;width:262px;font-size:3.6px;line-height:1.35;color:var(--muted)"><b style="color:var(--navy)">Preferred Vendors:</b> over 25 preferred and vetted vendors actively engaged and providing services across the senior living and care sector, ranging from energy and water efficiency to utility rebates and financing to rooftop and community solar</div>
  </div>
  <div class="abs foot"><i></i>Brovane</div>
  <div class="abs pgnum">3</div>
</section>

<section class="slide small s-vendors">
  <h2 class="abs heading" style="left:19px;top:18px">Representative Preferred Vendors</h2>
  <svg class="abs" style="left:0;top:0" width="305" height="227"><polygon points="162,77 198,113 162,149 126,113" fill="#e3e3e3"/></svg>
  <div class="vendor" style="left:162px;top:113px;font-size:8px;font-weight:700;color:var(--navy)">Brovane</div>
  <div class="vendor" style="left:123px;top:48px">Veldmark</div>
  <div class="vendor" style="left:179px;top:48px">Xenthra</div>
  <div class="vendor" style="left:65px;top:68px">Coolvane</div>
  <div class="vendor" style="left:127px;top:68px">Ampryn</div>
  <div class="vendor" style="left:182px;top:68px">Bluvale</div>
  <div class="vendor" style="left:232px;top:67px">Solvantis</div>
  <div class="vendor" style="left:51px;top:95px">Carelume</div>
  <div class="vendor" style="left:102px;top:90px">Airveso</div>
  <div class="vendor" style="left:212px;top:89px">Trestle Renewable</div>
  <div class="vendor" style="left:258px;top:89px">Tunova</div>
  <div class="vendor" style="left:91px;top:114px">Aerovell</div>
  <div class="vendor" style="left:226px;top:112px">Metrava</div>
  <div class="vendor" style="left:48px;top:125px">Tallmere Fund</div>
  <div class="vendor" style="left:257px;top:125px">Gridova</div>
  <div class="vendor" style="left:104px;top:133px">Aquarindo</div>
  <div class="vendor" style="left:211px;top:134px">Climetra</div>
  <div class="vendor" style="left:64px;top:151px">Verdalux</div>
  <div class="vendor" style="left:121px;top:154px">Chillmont</div>
  <div class="vendor" style="left:183px;top:154px">Prentwell Supply</div>
  <div class="vendor" style="left:247px;top:154px">Crestvane HVAC</div>
  <div class="vendor" style="left:90px;top:171px">Rainvale</div>
  <div class="vendor" style="left:154px;top:174px">Flowkeep</div>
  <div class="vendor" style="left:210px;top:172px">Kindora</div>
  <div class="vendor" style="left:129px;top:196px">Wellbrix</div>
  <div class="vendor" style="left:180px;top:196px">Dwellab</div>
  <div class="abs foot"><i></i>Brovane</div>
  <div class="abs pgnum">4</div>
</section>

<section class="slide small s-levels">
  <h2 class="abs heading" style="left:19px;top:18px;color:#fff">Multi-Level Approach to Building Efficiency</h2>
  <div class="abs" style="left:19px;top:35px;font-size:5px;color:#fff">Energy and water Savings Potential</div>
  <svg class="abs" style="left:0;top:0" width="305" height="227">
    <polygon points="43,58 81,48 119,58" fill="#6cc0ee"/>
    <rect x="101" y="50" width="5" height="8" fill="#6cc0ee"/>
    <rect x="47" y="58" width="68" height="46" fill="#6cc0ee"/>
    <rect x="47" y="104" width="68" height="32" fill="#a9c5ea"/>
    <rect x="47" y="136" width="68" height="25" fill="#7ea2de"/>
    <rect x="47" y="161" width="68" height="24" fill="#4f74c8"/>
    <rect x="47" y="185" width="68" height="20" fill="#1b3d9a"/>
    <g fill="none" stroke="#fff" stroke-width="0.8">
      <rect x="92" y="85" width="9" height="8"/><rect x="92" y="117" width="9" height="7"/><rect x="92" y="145" width="9" height="7"/><circle cx="96" cy="170" r="3.5"/><circle cx="96" cy="194" r="3"/>
    </g>
  </svg>
  <div class="pct" style="top:72px;font-size:16px">50<sup>%</sup></div>
  <div class="pct" style="top:110px;font-size:13px">40<sup>%</sup></div>
  <div class="pct" style="top:140px;font-size:12px">30<sup>%</sup></div>
  <div class="pct" style="top:165px;font-size:10px">20<sup>%</sup></div>
  <div class="pct" style="top:188px;font-size:8px">10<sup>%</sup></div>
  <div class="lvl-txt" style="top:82px">Smart whole building strategy including solar, Battery Storage and EV charging stations</div>
  <div class="lvl-line" style="top:104px"></div>
  <div class="lvl-txt" style="top:115px">Efficient capital replacement strategy including HVAC, Mechanicals, Building Envelope and Roofing</div>
  <div class="lvl-line" style="top:136px"></div>
  <div class="lvl-txt" style="top:144px">Enhanced HVAC maintenance, insulation, and efficiency technology such as Smart Thermostats, Smart Motors and Chips</div>
  <div class="lvl-line" style="top:161px"></div>
  <div class="lvl-txt" style="top:169px">Practical whole building technology such as Water Efficiency Valves and Power Grid Filters</div>
  <div class="lvl-line" style="top:185px"></div>
  <div class="lvl-txt" style="top:190px">Initial LED lighting and Water Efficiency Improvements such as low flow plumbing fixtures, smart irrigation &amp; landscape</div>
  <div class="abs foot"><i></i>Brovane</div>
  <div class="abs pgnum">5</div>
</section>

<section class="slide small s-rule">
  <div class="side">
    <div class="chart" style="top:52px">
      <div class="ct">Electricity End Uses</div>
      <svg class="abs" style="left:22px;top:9px" width="38" height="38" viewBox="0 0 38 38">
        <circle cx="19" cy="19" r="14" fill="none" stroke="#ddd" stroke-width="8"/>
        <circle cx="19" cy="19" r="14" fill="none" stroke="#d3333a" stroke-width="8" stroke-dasharray="15.8 72.2" transform="rotate(-90 19 19)"/>
        <circle cx="19" cy="19" r="14" fill="none" stroke="#d3333a" stroke-width="8" stroke-dasharray="15.8 72.2" stroke-dashoffset="-44" transform="rotate(-90 19 19)"/>
        <circle cx="19" cy="19" r="14" fill="none" stroke="#888" stroke-width="8" stroke-dasharray="17.6 70.4" stroke-dashoffset="-62" transform="rotate(-90 19 19)"/>
      </svg>
      <div class="leg" style="left:3px;top:10px">20% Misc<br>2% Computing<br>9% Office<br>9% Refrig<br>3% Cooking</div>
      <div class="leg" style="right:3px;top:8px;text-align:right">Heating 5%<br>Cooling 15%<br><br>Ventilation 18%<br>Water 1%<br>Lighting 18%</div>
    </div>
    <div class="chart" style="top:113px">
      <div class="ct">Natural Gas End Uses</div>
      <svg class="abs" style="left:22px;top:9px" width="38" height="38" viewBox="0 0 38 38">
        <circle cx="19" cy="19" r="14" fill="none" stroke="#ddd" stroke-width="8"/>
        <circle cx="19" cy="19" r="14" fill="none" stroke="#d3333a" stroke-width="8" stroke-dasharray="40.5 47.5" transform="rotate(-80 19 19)"/>
        <circle cx="19" cy="19" r="14" fill="none" stroke="#555" stroke-width="8" stroke-dasharray="5.3 82.7" stroke-dashoffset="-82.7" transform="rotate(-80 19 19)"/>
      </svg>
      <div class="leg" style="left:3px;top:10px">6% Cooking<br><br><br>46% Water</div>
      <div class="leg" style="right:3px;top:8px;text-align:right">Misc 2%<br><br><br>Heating 46%</div>
    </div>
    <div class="abs" style="left:10px;top:165px;display:flex;align-items:center;gap:2px;font-size:4.5px;font-weight:700;color:#333"><i style="width:5px;height:5px;background:var(--red);display:block"></i>Plainsworth Energy</div>
    <div class="abs" style="left:7px;top:185px;font-size:3.6px;line-height:1.35;color:var(--accent)">* Average EUI for Nursing<br>Homes in the Midwest</div>
  </div>
  <h2 class="abs heading rule-title">E-Playbook - 80/20 Energy Efficiency Rule</h2>
  <div class="abs" style="left:19px;top:36px;width:180px;font-size:4.6px;font-weight:600;line-height:1.3;color:var(--navy)">In Senior Living &amp; Care, HVAC, Lighting, and Water Heating typically accounts for up to 80% of energy use*:</div>
  <div class="abs sub6" style="left:19px;top:54px">Electricity uses</div>
  <div class="cells" style="top:61px;grid-template-columns:repeat(5,1fr)">
    <div class="cell"><div class="v">18<sup>%</sup></div><div class="k">lighting</div></div>
    <div class="cell"><div class="v">1<sup>%</sup></div><div class="k">water heating</div></div>
    <div class="cell"><div class="v">18<sup>%</sup></div><div class="k">ventilation</div></div>
    <div class="cell"><div class="v">15<sup>%</sup></div><div class="k">space cooling</div></div>
    <div class="cell"><div class="v">5<sup>%</sup></div><div class="k">space heating</div></div>
  </div>
  <div class="cells" style="top:80px;grid-template-columns:repeat(5,1fr)">
    <div class="cell"><div class="v">20<sup>%</sup></div><div class="k">miscellaneous</div></div>
    <div class="cell"><div class="v">2<sup>%</sup></div><div class="k">computing</div></div>
    <div class="cell"><div class="v">9<sup>%</sup></div><div class="k">office equipment</div></div>
    <div class="cell"><div class="v">9<sup>%</sup></div><div class="k">refrigeration</div></div>
    <div class="cell"><div class="v">3<sup>%</sup></div><div class="k">cooking</div></div>
  </div>
  <div class="abs sub6" style="left:19px;top:104px">Natural gas uses</div>
  <div class="cells green" style="top:111px;grid-template-columns:repeat(4,1fr)">
    <div class="cell"><div class="v">46<sup>%</sup></div><div class="k">water heating</div></div>
    <div class="cell"><div class="v">46<sup>%</sup></div><div class="k">space heating</div></div>
    <div class="cell"><div class="v">2<sup>%</sup></div><div class="k">miscellaneous</div></div>
    <div class="cell"><div class="v">6<sup>%</sup></div><div class="k">cooking</div></div>
  </div>
  <div class="abs sub6" style="left:19px;top:138px;font-style:italic">HVAC Lesson Learned:</div>
  <ul class="bullets">
    <li>Single largest equipment investment at most properties, often over <b>$1million+</b></li>
    <li>Up to <b>60%</b> of total energy cost</li>
    <li>It is not just the upfront or replacement cost but the total cost of ownership, including maintenance, preservation, and efficiency</li>
    <li>Proper maintenance is a critical component to overall efficiency, preservation, and ownership cost</li>
    <li>You need to stay on top of issues and plan ahead</li>
    <li>If you make a mistake, you will have to live with it for the next 15 years (less if you don't maintain it)</li>
    <li>Operators need to be both Care and Real Estate focused</li>
  </ul>
  <div class="abs foot"><i></i>Brovane</div>
  <div class="abs pgnum">6</div>
</section>

<section class="slide small s-talk">
  <div class="abs talk-brand"><i></i>Brovane</div>
  <div class="abs talk-title"><div class="l1">Let's Have</div><div class="l2">A Discussion</div></div>
  <div class="abs people" role="img" aria-label="Illustration of four people seated on stools having a conversation"></div>
</section>

</body>
</html>
```